NEW Modern Sleek Business Card for VR Language Startup

Our startup is using VR to lead the next wave of world language education. We need a two-sided business card that introduces the larger organization (Quorvel Language Inc) and our contact info on one side and shows the product, Lumidrasca, on the other side.

Side 1 (contact info)= Quorvel Logo and Contact info (name, title, phone, email)

Side 2 (product)= Lumidrasc logo, text, and website
Text= Culturally Immersive Language Learning Games
Website= www.lumidrasc.example

Target Market(s)

Education, Technology

Contact Information for Business Card

Contact info will be updated upon approval of the design. For now, put this as a placeholder.

Perry Hollins
Founder & CEO
phollins@mailtrove.example
(555)-014-2736

Font styles to use
Other font styles liked:
• Gibson and Century Gothic are the brand fonts

Requirements
Nice to have
• I would love to see cohesion between the design and colors of the two logos. I have attached a few business card designs that I like, so you can get a feel for my preferred style.

```html
<!DOCTYPE html>
<html lang="en">
<head>
<meta charset="utf-8">
<title>Quorvel Language — Business Card</title>
<link rel="stylesheet" href="https://fonts.googleapis.com/css2?family=Didact+Gothic&display=swap">
<style>
  :root {
    --canvas: #e8e9eb;
    --card-front: #0b0b0c;
    --card-back: #1c1e21;
    --backdrop-shade: #2a2d31;
    --text-light: #f4f4f6;
    --text-muted: #c3c6cc;
    --accent-blue: #3d8fe0;
    --accent-warm: #f0466c;
    --glow-orange: #f7a536;
    --glow-pink: #ee3f63;
    --glow-violet: #8a5cc8;
    --glow-cyan: #32b8ee;
    --rule: #9a9da3;
    --font-body: "Didact Gothic", sans-serif;
  }
  * { box-sizing: border-box; margin: 0; padding: 0; }
  html, body { width: 1200px; height: 900px; overflow: hidden; }
  body {
    background: var(--canvas);
    font-family: var(--font-body);
    display: flex;
    align-items: center;
    justify-content: center;
    gap: 40px;
  }
  .card {
    width: 540px;
    height: 309px;
    position: relative;
    overflow: hidden;
    color: var(--text-light);
  }

  /* Front: company + contact */
  .card--front { background: var(--card-front); }
  .front-glow {
    position: absolute;
    right: -30px;
    top: -20px;
    width: 300px;
    height: 350px;
    border-radius: 50%;
    background:
      radial-gradient(ellipse at 30% 25%, var(--glow-orange) 0%, transparent 55%),
      radial-gradient(ellipse at 55% 50%, var(--glow-pink) 0%, transparent 55%),
      radial-gradient(ellipse at 70% 75%, var(--glow-cyan) 0%, transparent 55%),
      radial-gradient(ellipse at 50% 50%, var(--glow-violet) 0%, transparent 70%);
    opacity: .85;
    filter: blur(18px);
  }
  .brand {
    position: absolute;
    left: 38px;
    top: 88px;
    display: flex;
    align-items: center;
    gap: 14px;
  }
  .brand__dot {
    width: 40px; height: 40px;
    border-radius: 50%;
    background: var(--accent-warm);
  }
  .brand__name {
    font-size: 24px;
    letter-spacing: 5px;
    line-height: 1;
  }
  .brand__name span {
    display: block;
    font-size: 12px;
    letter-spacing: 7px;
    margin-top: 5px;
  }
  .contact {
    position: absolute;
    left: 38px;
    top: 178px;
  }
  .contact__name { font-size: 16px; letter-spacing: .5px; }
  .contact__title { font-size: 13px; color: var(--accent-blue); margin-top: 2px; }
  .contact__list { list-style: none; margin-top: 16px; }
  .contact__item {
    display: flex; align-items: center; gap: 9px;
    font-size: 13px; margin-bottom: 8px;
  }
  .contact__icon {
    width: 16px; height: 16px; border-radius: 50%;
    background: var(--accent-blue);
    display: flex; align-items: center; justify-content: center;
    flex: none;
  }

  /* Back: product */
  .card--back { background: var(--card-back); }
  .back-backdrop {
    position: absolute;
    left: -80px;
    top: 40px;
    width: 400px;
    height: 360px;
    border-radius: 50%;
    background: radial-gradient(ellipse at 60% 45%, var(--backdrop-shade) 0%, var(--card-back) 72%);
  }
  .product {
    position: absolute;
    left: 0; right: 0; top: 88px;
    display: flex; flex-direction: column; align-items: center;
  }
  .product__mark { display: flex; align-items: center; gap: 12px; }
  .product__dot { width: 34px; height: 34px; border-radius: 50%; background: var(--accent-blue); }
  .product__name { font-size: 34px; letter-spacing: .5px; }
  .product__rule { width: 330px; height: 1px; background: var(--rule); margin: 16px 0 10px; }
  .product__tagline { font-size: 14px; letter-spacing: .3px; }
  .product__url { font-size: 12px; color: var(--text-muted); margin-top: 8px; letter-spacing: .5px; }
  .product__rule--bottom { width: 200px; margin: 12px 0 0; }
</style>
</head>
<body>
  <section class="card card--front" aria-label="Business card front">
    <div class="front-glow" role="img" aria-label="Large brand gradient decoration in orange, pink, violet and cyan"></div>
    <div class="brand">
      <div class="brand__dot"></div>
      <div class="brand__name">QUORVEL<span>LANGUAGE</span></div>
    </div>
    <div class="contact">
      <p class="contact__name">Perry HOLLINS</p>
      <p class="contact__title">Founder | CEO</p>
      <ul class="contact__list">
        <li class="contact__item">
          <span class="contact__icon">
            <svg width="9" height="9" viewBox="0 0 24 24" fill="#fff"><path d="M6.6 10.8a15.1 15.1 0 006.6 6.6l2.2-2.2a1 1 0 011-.25 11.4 11.4 0 003.6.57 1 1 0 011 1V20a1 1 0 01-1 1A17 17 0 013 4a1 1 0 011-1h3.5a1 1 0 011 1 11.4 11.4 0 00.57 3.6 1 1 0 01-.25 1z"/></svg>
          </span>
          (555)-014-2736
        </li>
        <li class="contact__item">
          <span class="contact__icon">
            <svg width="9" height="9" viewBox="0 0 24 24"><rect x="2" y="5" width="20" height="14" fill="#fff"/><path d="M3 6l9 7 9-7" fill="none" stroke="#3d8fe0" stroke-width="2"/></svg>
          </span>
          phollins@mailtrove.example
        </li>
      </ul>
    </div>
  </section>

  <section class="card card--back" aria-label="Business card back">
    <div class="back-backdrop" role="img" aria-label="Dark tonal backdrop graphic with circuit motif"></div>
    <div class="product">
      <div class="product__mark">
        <div class="product__dot"></div>
        <div class="product__name">Lumidrasc</div>
      </div>
      <div class="product__rule"></div>
      <p class="product__tagline">Culturally Immersive Language Learning Games</p>
      <p class="product__url">www.lumidrasc.example</p>
      <div class="product__rule product__rule--bottom"></div>
    </div>
  </section>
</body>
</html>
```